Banner Ad Design Project

This is a banner Ad Design for MindHarbor 2013, a conference and e-Expo in August 2013 to be held at the Kestrel Bay Events Centre. The conference's focus is on mental excellence and Brain Health. This conference is bringing together personal and community needs, scientific knowledge, and dedicated professionals to create support and solutions for mental excellence and brain-related health issues. Right now in North America, one out of every two individuals is affected by mental health issues: depression, anxiety, learning disorders, memory loss to name a few.
Who we are:
Organization: Willow Lantern Foundation
Industry: Non-profit
Target Market(s)
Age group above 18, parents and health professionals, managers.
Industry/Entity Type
Mental Health
Requirements
Must have
- Please follow the warm design grey as in the design samples.
Nice to have
- Buy tickets and ask your unique questions to the medical panel! Seats are limited!

```html
<!DOCTYPE html>
<html lang="en">
<head>
<meta charset="utf-8">
<title>MindHarbor 2013 Banner Ad</title>
<link href="https://fonts.googleapis.com/css2?family=Oswald:wght@500;600&family=Arimo:wght@400;700&display=swap" rel="stylesheet">
<style>
  :root {
    --backdrop: #e3c39b;
    --white: #ffffff;
    --navy: #2f3a86;
    --orange-deep: #e5560c;
    --orange-light: #f7921e;
    --purple: #7b3f8c;
    --purple-text: #6a2f86;
    --button-top: #f7941d;
    --button-bottom: #e9620f;
    --divider: #5c2c6b;
  }
  * { box-sizing: border-box; margin: 0; padding: 0; }
  html, body { width: 1200px; height: 576px; overflow: hidden; }
  body { background: var(--backdrop); position: relative; font-family: "Arimo", Arial, sans-serif; }

  .banner {
    position: absolute; left: 60px; width: 1076px; height: 133px;
    background: var(--white); overflow: hidden;
    box-shadow: 0 2px 6px rgba(0,0,0,0.18);
  }
  .banner--first { top: 134px; }
  .banner--second { top: 288px; }

  .brand { position: absolute; left: 22px; top: 30px; display: flex; align-items: center; gap: 10px; }
  .brand__dot { width: 52px; height: 52px; border-radius: 50%; background: var(--navy); flex: none; }
  .brand__text { display: flex; flex-direction: column; }
  .brand__name { font-family: "Arimo", Arial, sans-serif; font-weight: 700; font-size: 31px; line-height: 1.05; color: var(--navy); }
  .brand__tagline { font-family: "Arimo", Arial, sans-serif; font-weight: 700; font-size: 12px; color: var(--navy); margin-top: 3px; }

  .offer {
    position: absolute; left: 430px; top: 0; width: 438px; height: 100%;
    background: linear-gradient(90deg, var(--orange-deep) 0%, var(--orange-light) 100%);
  }
  .portrait {
    position: absolute; left: 318px; top: 0; width: 176px; height: 100%;
    background: linear-gradient(180deg, #c9c2bb 0%, #d8a98a 45%, #9fb6cf 75%, #7f9fc4 100%);
    border-radius: 88px 88px 0 0;
  }
  .headline {
    position: absolute; left: 461px; top: 12px; width: 400px;
    font-family: "Oswald", sans-serif; font-weight: 500; font-size: 26px; line-height: 1.18;
    color: var(--white); text-transform: uppercase; letter-spacing: 0.2px;
  }
  .headline__accent { color: var(--purple-text); }
  .details {
    position: absolute; left: 495px; top: 84px; width: 340px;
    font-size: 12.5px; line-height: 17px; color: var(--white); white-space: nowrap;
  }
  .banner--second .details { color: var(--purple-text); }

  .cta {
    position: absolute; left: 868px; top: 0; width: 208px; height: 100%;
    background: var(--purple); border-left: 2px solid var(--divider);
  }
  .cta__tag {
    position: absolute; left: 22px; top: 28px; width: 163px; height: 30px;
    background: var(--white); transform: rotate(-2deg);
    font-size: 16px; color: var(--purple-text); text-align: center; line-height: 30px;
    box-shadow: 0 1px 3px rgba(0,0,0,0.3);
  }
  .cta__button {
    position: absolute; left: 22px; top: 66px; width: 163px; height: 48px;
    background: linear-gradient(180deg, var(--button-top), var(--button-bottom));
    border-radius: 3px; color: var(--white); font-size: 20px; text-align: center; line-height: 48px;
    box-shadow: 0 2px 3px rgba(0,0,0,0.3);
  }
</style>
</head>
<body>
  <section class="banner banner--first">
    <div class="brand">
      <span class="brand__dot"></span>
      <div class="brand__text">
        <span class="brand__name">MindHarbor.ca</span>
        <span class="brand__tagline">Clear minds. Healthy lives.</span>
      </div>
    </div>
    <div class="offer"></div>
    <div class="portrait" role="img" aria-label="Portrait of a smiling medical panel speaker"></div>
    <h2 class="headline"><span class="headline__accent">Buy tickets</span> and ask your unique questions to the medical panel!</h2>
    <p class="details">The conference and e-Expo will be held at the<br>Kestrel Bay Events Centre in august 2013.</p>
    <div class="cta">
      <div class="cta__tag">seats are limited!</div>
      <div class="cta__button">JOIN NOW</div>
    </div>
  </section>

  <section class="banner banner--second">
    <div class="brand">
      <span class="brand__dot"></span>
      <div class="brand__text">
        <span class="brand__name">MindHarbor.ca</span>
        <span class="brand__tagline">Clear minds. Healthy lives.</span>
      </div>
    </div>
    <div class="offer"></div>
    <div class="portrait" role="img" aria-label="Portrait of a smiling medical panel speaker"></div>
    <h2 class="headline"><span class="headline__accent">Buy tickets</span> and ask your unique questions to the medical panel!</h2>
    <p class="details">The conference and e-Expo will be held at the<br>Kestrel Bay Events Centre in august 2013.</p>
    <div class="cta">
      <div class="cta__tag">seats are limited!</div>
      <div class="cta__button">JOIN NOW</div>
    </div>
  </section>
</body>
</html>
```